The maple crew

I want it as prefession and attractive as possible we are a lawnmowing business

Phone number 605-318-2264
Name- Carlos Whitfield
Email- themaplecrewsd@fernpost.com

```html
<!DOCTYPE html>
<html lang="en">
<head>
<meta charset="UTF-8">
<title>The maple crew – Business Card</title>
<link href="https://fonts.googleapis.com/css2?family=Montserrat:wght@400;500;700&display=swap" rel="stylesheet">
<style>
  :root {
    --forest: #0a5e3a;
    --leaf: #3aa845;
    --ink: #1c1c1c;
    --paper: #ffffff;
    --backdrop: #e9e6e1;
  }
  html, body {
    margin: 0;
    padding: 0;
    width: 900px;
    height: 1200px;
    overflow: hidden;
    background: var(--backdrop);
    font-family: "Montserrat", Arial, sans-serif;
  }
  .canvas {
    position: relative;
    width: 900px;
    height: 1200px;
  }
  .card {
    position: absolute;
    width: 742px;
    height: 440px;
    border-radius: 24px;
    overflow: hidden;
    box-shadow: 0 10px 24px rgba(0,0,0,0.18);
  }
  .card-front {
    left: 80px;
    top: 131px;
    background: var(--paper);
  }
  .card-back {
    left: 78px;
    top: 638px;
    background: var(--forest);
  }
  .front-band {
    position: absolute;
    left: 0;
    top: 61px;
    width: 417px;
    height: 77px;
    background: var(--forest);
  }
  .front-wordmark {
    position: absolute;
    left: 424px;
    top: 61px;
    width: 258px;
    height: 77px;
    display: flex;
    align-items: center;
    justify-content: center;
    font-weight: 700;
    font-size: 27px;
    color: var(--forest);
    white-space: nowrap;
  }
  .contact-block {
    position: absolute;
    left: 41px;
    top: 290px;
  }
  .person-name {
    margin: 0;
    font-size: 26px;
    font-weight: 700;
    line-height: 1.1;
  }
  .person-name .first { color: var(--leaf); }
  .person-name .last { color: var(--forest); }
  .person-role {
    margin: 6px 0 18px;
    font-size: 16px;
    font-weight: 500;
    color: var(--ink);
  }
  .contact-line {
    display: flex;
    align-items: center;
    gap: 10px;
    font-size: 16px;
    color: var(--ink);
    margin-bottom: 9px;
  }
  .contact-line svg { width: 16px; height: 14px; fill: var(--leaf); }
  .back-wordmark {
    position: absolute;
    inset: 0;
    display: flex;
    align-items: center;
    justify-content: center;
    font-weight: 700;
    font-size: 56px;
    color: var(--paper);
    white-space: nowrap;
  }
</style>
</head>
<body>
<main class="canvas">
  <section class="card card-front">
    <div class="front-band"></div>
    <div class="front-wordmark">The maple crew</div>
    <div class="contact-block">
      <h1 class="person-name"><span class="first">Carlos</span> <span class="last">Whitfield</span></h1>
      <p class="person-role">Managing Director</p>
      <div class="contact-line">
        <svg viewBox="0 0 16 14" aria-hidden="true"><path d="M2 3c0-1 1-2 6-2s6 1 6 2v1h-3V3H5v1H2z"/><path d="M4 5h8l2 8H2z"/></svg>
        <span>605-318-2264</span>
      </div>
      <div class="contact-line">
        <svg viewBox="0 0 16 14" aria-hidden="true"><path d="M1 2h14v1L8 8 1 3z"/><path d="M1 5l7 5 7-5v7H1z"/></svg>
        <span>themaplecrewsd@fernpost.com</span>
      </div>
    </div>
  </section>
  <section class="card card-back">
    <div class="back-wordmark">The maple crew</div>
  </section>
</main>
</body>
</html>
```